Formal letterhead for Commercial Real Estate Company

Formal and professional letterhead for the transactional documents of a commercial real estate company.

Elements to be Included between header and footer:

- Logo (attached)(should be applied without the yellow background, in other words, the background colour for the design should be white)
- Slogan: Your Property Solution
- Physical Address: 41 Tennant Lane, Oakridge, Durban, 4001
- Postal Address: PO Box 72814, Fernhill, 4062
- Phone: 031 648 9125
- Fax: 031 573 4189
- Website: www.delvane.co.zaz
- eMail: contact@delvane.co.za

The brand guide is attached (the one you last provided), it does not provide direction on letterhead specifically but on other brand aspects.

Industry/Entity Type

Real Estate

```html
<!DOCTYPE html>
<html lang="en">
<head>
<meta charset="utf-8">
<title>Delvane Letterhead</title>
<link rel="stylesheet" href="https://fonts.googleapis.com/css2?family=Josefin+Sans:wght@300&family=Open+Sans:ital,wght@0,400;1,400&display=swap">
<style>
  :root {
    --backdrop: #d6d7d4;
    --paper: #ffffff;
    --ink: #1a1a1a;
    --charcoal: #58595b;
    --brand-yellow: #f2df1c;
    --muted: #555555;
  }
  html, body {
    margin: 0;
    padding: 0;
    width: 1200px;
    height: 784px;
    overflow: hidden;
    background: var(--backdrop);
  }
  .letterhead {
    position: absolute;
    left: 338px;
    top: 22px;
    width: 523px;
    height: 740px;
    background: var(--paper);
    box-shadow: 0 2px 6px rgba(0,0,0,0.18);
    overflow: hidden;
  }
  .corner-accent {
    position: absolute;
    inset: 0;
    width: 100%;
    height: 100%;
  }
  .brand {
    position: absolute;
    left: 26px;
    top: 40px;
    display: flex;
    align-items: center;
    gap: 8px;
  }
  .brand-mark {
    width: 14px;
    height: 14px;
    background: var(--ink);
  }
  .brand-name {
    font-family: "Josefin Sans", sans-serif;
    font-weight: 300;
    font-size: 24px;
    letter-spacing: 3px;
    color: var(--ink);
    line-height: 1;
    padding-top: 4px;
  }
  .slogan {
    position: absolute;
    right: 26px;
    top: 52px;
    margin: 0;
    font-family: "Josefin Sans", sans-serif;
    font-weight: 300;
    font-size: 17px;
    letter-spacing: 3px;
    color: var(--muted);
  }
  .slogan .highlight {
    color: var(--brand-yellow);
  }
  .contact-line {
    position: absolute;
    left: 18px;
    bottom: 16px;
    margin: 0;
    font-family: "Open Sans", sans-serif;
    font-style: italic;
    font-size: 6.6px;
    color: var(--muted);
    white-space: nowrap;
    display: flex;
    align-items: center;
    gap: 4px;
  }
  .contact-line .dot {
    width: 4px;
    height: 4px;
    border-radius: 50%;
    background: var(--charcoal);
    display: inline-block;
  }
</style>
</head>
<body>
  <main class="letterhead">
    <svg class="corner-accent" viewBox="0 0 523 740" preserveAspectRatio="none" aria-hidden="true">
      <polygon points="0,0 222,0 0,34" fill="var(--charcoal)"/>
      <polygon points="523,740 262,740 523,646" fill="var(--brand-yellow)"/>
    </svg>

    <header class="brand">
      <span class="brand-mark"></span>
      <span class="brand-name">DELVANE</span>
    </header>

    <p class="slogan">Your <span class="highlight">PROPERTY</span> Solution</p>

    <footer class="contact-line">
      <span class="dot"></span><span>41 Tennant Lane, Oakridge, Durban, 4001</span>
      <span class="dot"></span><span>PO Box 72814, Fernhill, 4062</span>
      <span class="dot"></span><span>031 648 9125</span>
      <span class="dot"></span><span>031 573 4189</span>
      <span class="dot"></span><span>contact@delvane.co.za</span>
      <span class="dot"></span><span>www.delvane.co.zaz</span>
    </footer>
  </main>
</body>
</html>
```